Divi Theme Wordpress Web Design

Hi,

We have had a Divi theme website running on Wordpress for a few years but need a fresh refresh.

Designs must be possible with standard Divi theme and minimal/no CSS customisation or similar. if this is required please note this in submission. Also, please note mobile and device usage which must be universal.

We have our logo files attached, plus some research and sample sites we have done, plus all of our current collateral. We will need a few examples such as landing (main) page, single blog post and software specific page. See current examples below:

Landing (Main) - http://www.vantrelworks.com/inventory-wholesale-manufacturing/

Single Blog Post - http://www.vantrelworks.com/why-remote-work-made-break-most-relaxing-ever/

Software Page - http://www.vantrelworks.com/software-implementation/plume-stockroom-implementation-and-training/

Target Market(s)

small businesses, small business owners, people who need simple but technical computer help,

Industry/Entity Type

Professional Service

Number of Pages Required

3 page

Requirements
Must have
• see attachment guide
Nice to have
• see attachment guide

```html
<!DOCTYPE html>
<html lang="en">
<head>
<meta charset="utf-8">
<title>Vantrel Works</title>
<link rel="stylesheet" href="https://fonts.googleapis.com/css2?family=Raleway:wght@400;500;600;700&family=Open+Sans:wght@400;600;700&display=swap">
<style>
:root{
  --orange:#f0873a;
  --teal:#1ab5c1;
  --red:#a3212a;
  --navy:#1b5a85;
  --band:#0d5a8a;
  --ink:#2b2b2b;
  --muted:#6f6f6f;
  --light:#f5f5f5;
  --cell:#f2f2f2;
  --line:#d6d6d6;
}
*{box-sizing:border-box;margin:0;padding:0}
html,body{width:1200px;height:3448px;overflow:hidden;background:#fff}
body{position:relative;font-family:"Open Sans",Arial,sans-serif;color:var(--ink)}
.abs{position:absolute}
h1,h2,h3{font-family:"Raleway",Arial,sans-serif}

/* hero */
.hero{left:0;top:0;width:1200px;height:552px;background:linear-gradient(120deg,#8a8d90 0%,#c9c6c0 40%,#6f7278 70%,#3f4247 100%)}
.hero-shade{left:0;top:0;width:1200px;height:552px;background:rgba(20,25,30,.28)}
.nav-brand{left:100px;top:22px;display:flex;align-items:center;gap:12px;color:#fff;font-family:"Raleway",sans-serif;font-weight:700;font-size:27px}
.nav-brand i{width:40px;height:40px;border-radius:50%;background:#fff;display:block}
.nav{top:32px;right:100px;display:flex;gap:44px;color:#fff;font-family:"Raleway",sans-serif;font-weight:600;font-size:16px;align-items:center}
.nav-line{left:0;top:86px;width:1200px;height:1px;background:rgba(255,255,255,.25)}
.hero-title{left:0;top:180px;width:1200px;text-align:center;color:#fff;font-size:66px;font-weight:600}
.hero-sub{left:0;top:276px;width:1200px;text-align:center;color:#fff;font-size:16px;line-height:32px}
.dots{left:0;top:480px;width:1200px;display:flex;justify-content:center;gap:6px}
.dots i{width:14px;height:14px;border-radius:50%;border:2px solid #fff;display:block}
.dots i:first-child{background:#fff}

/* feature tiles */
.tile{top:566px;height:212px;color:#fff;text-align:center;font-size:19px;line-height:32px;padding-top:30px}
.tile svg{display:block;margin:0 auto 20px}
.tile-orange{left:0;width:393px;background:var(--orange)}
.tile-teal{left:405px;width:391px;background:var(--teal)}
.tile-red{left:807px;width:393px;background:var(--red)}

/* trust */
.section-title{left:0;width:1200px;text-align:center;font-weight:700;font-size:32px;color:var(--ink)}
.question{width:240px;text-align:center;top:968px}
.question .ring{width:148px;height:148px;border:2px solid var(--line);border-radius:50%;margin:0 auto 34px;display:flex;align-items:center;justify-content:center}
.question p{font-size:16px;line-height:30px;color:var(--ink)}

/* process */
.process-side{left:0;top:1302px;width:600px;height:595px;background:var(--light)}
.process-photo{left:600px;top:1302px;width:600px;height:595px;background:linear-gradient(135deg,#f4f5f7 0%,#dfe3e8 45%,#8fa0b6 60%,#eef0f2 80%,#d9dcdf 100%)}
.process-title{left:99px;top:1340px;font-size:32px;font-weight:700}
.process-intro{left:99px;top:1398px;width:470px;font-size:12px;line-height:23px;color:var(--muted)}
.step{left:96px;display:flex;gap:28px;align-items:center}
.step .num{width:76px;height:76px;border:2px solid #c9c9c9;border-radius:50%;display:flex;align-items:center;justify-content:center;font-family:"Raleway",sans-serif;font-size:34px;font-weight:600;color:var(--navy)}
.step h3{font-size:20px;font-weight:600;margin-bottom:6px}
.step p{font-size:11.5px;line-height:21px;color:var(--muted);width:370px}

/* clients */
.clients-sub{left:0;top:2052px;width:1200px;text-align:center;font-size:13px;color:var(--muted)}
.client{width:172px;height:86px;background:var(--cell);display:flex;align-items:center;justify-content:center;font-family:"Open Sans",sans-serif;font-weight:600;font-size:17px;color:#333;gap:8px}
.client i{width:16px;height:16px;background:#333;display:block}

/* testimonials */
.band{left:0;top:2544px;width:1200px;height:338px;background:var(--band)}
.band-title{left:0;top:2600px;width:1200px;text-align:center;color:#fff;font-size:32px;font-weight:600}
.quote{top:2684px;display:flex;gap:26px;color:#fff;width:340px}
.avatar{flex:none;width:76px;height:76px;border-radius:50%;border:3px solid #fff;background:linear-gradient(160deg,#c9b8a6,#7b6a5f)}
.quote blockquote{font-size:13px;line-height:26px;font-style:italic;padding-top:2px}
.quote blockquote b{font-family:Georgia,serif;font-size:22px;font-style:normal;margin-right:6px}
.quote .who{font-size:10px;font-weight:700;margin-top:18px;font-style:normal;text-transform:uppercase}
.quote .role{font-size:9px;font-style:italic}

/* contact */
.form-title{left:99px;top:3070px;font-size:18px;font-weight:600}
.field{height:32px;border:1px solid #cfcfcf;font-size:10px;color:#888;padding:8px 10px;text-transform:uppercase}
.submit{left:628px;top:3356px;width:74px;height:32px;border-radius:16px;background:var(--teal);color:#fff;font-size:11px;font-weight:700;display:flex;align-items:center;justify-content:center}
.info-title{left:782px;top:3070px;font-size:18px;font-weight:600}
.info{left:782px;display:flex;align-items:center;gap:22px;font-size:11px;line-height:20px;color:#555}
.info .ic{width:34px;height:34px;border:1px solid #cfcfcf;border-radius:50%;display:flex;align-items:center;justify-content:center;flex:none}
.social{left:782px;top:3286px;display:flex;gap:6px}
.social i{width:28px;height:28px;border-radius:50%;display:block}
.rule{left:99px;top:3363px;width:1002px;height:1px;background:#e1e1e1}
.copy{left:0;top:3396px;width:1200px;text-align:center;font-size:11px;color:#666}
</style>
</head>
<body>

<section class="abs hero" role="img" aria-label="Photo of hands holding a tablet in a warehouse"></section>
<div class="abs hero-shade"></div>
<div class="abs nav-brand"><i></i>Vantrel Works</div>
<nav class="abs nav"><span>Home</span><span>About Us</span><span>Blog</span><span>Software Solutions</span>
  <svg width="16" height="16" viewBox="0 0 16 16"><circle cx="6.5" cy="6.5" r="5" fill="none" stroke="#fff" stroke-width="2"/><line x1="10" y1="10" x2="15" y2="15" stroke="#fff" stroke-width="2.4"/></svg>
</nav>
<div class="abs nav-line"></div>
<h1 class="abs hero-title">Vantrel Works</h1>
<p class="abs hero-sub">Our Ledgerly Add-On Solutions help ambitious businesses who want to take control of their inventory<br>by removing the guess work and enabling them to make better decisions.</p>
<div class="abs dots"><i></i><i></i><i></i><i></i></div>

<div class="abs tile tile-orange">
  <svg width="84" height="72" viewBox="0 0 84 72" fill="#fff"><circle cx="30" cy="40" r="22"/><circle cx="30" cy="40" r="8" fill="var(--orange)"/><g stroke="#fff" stroke-width="9"><line x1="30" y1="12" x2="30" y2="68"/><line x1="2" y1="40" x2="58" y2="40"/><line x1="10" y1="20" x2="50" y2="60"/><line x1="50" y1="20" x2="10" y2="60"/></g><circle cx="30" cy="40" r="8" fill="var(--orange)"/><circle cx="66" cy="16" r="12"/><circle cx="66" cy="16" r="4" fill="var(--orange)"/><circle cx="68" cy="52" r="9"/><circle cx="68" cy="52" r="3" fill="var(--orange)"/></svg>
  Imagine having complete control<br>of your inventory
</div>
<div class="abs tile tile-teal">
  <svg width="60" height="72" viewBox="0 0 60 72" fill="#fff"><ellipse cx="30" cy="10" rx="28" ry="9"/><path d="M2 18c0 5 12.5 9 28 9s28-4 28-9v13c0 5-12.5 9-28 9S2 36 2 31z"/><path d="M2 38c0 5 12.5 9 28 9s28-4 28-9v13c0 5-12.5 9-28 9S2 56 2 51z"/></svg>
  Imagine having confidence in your<br>inventory data
</div>
<div class="abs tile tile-red">
  <svg width="72" height="72" viewBox="0 0 72 72" fill="none" stroke="#fff" stroke-width="9"><path d="M60 28A26 26 0 0 0 14 22"/><path d="M12 44a26 26 0 0 0 46 6"/><path d="M64 8v22H42" fill="#fff" stroke="none"/><path d="M8 64V42h22" fill="#fff" stroke="none"/></svg>
  Imagine never having another<br>inventory nightmare again
</div>

<h2 class="abs section-title" style="top:872px">Do you REALLY trust your inventory system?</h2>
<div class="abs question" style="left:69px"><div class="ring"><svg width="66" height="50" viewBox="0 0 66 50"><path d="M4 46V20l14 10 16-26 14 18 14-8v32z" fill="var(--navy)"/><path d="M2 2v46h62" stroke="var(--navy)" stroke-width="3" fill="none"/></svg></div><p>Are those stock levels<br>accurate?</p></div>
<div class="abs question" style="left:342px"><div class="ring"><svg width="40" height="58" viewBox="0 0 40 58"><rect x="4" y="2" width="32" height="54" fill="var(--navy)"/><g fill="#fff"><rect x="10" y="8" width="6" height="6"/><rect x="24" y="8" width="6" height="6"/><rect x="10" y="20" width="6" height="6"/><rect x="24" y="20" width="6" height="6"/><rect x="10" y="32" width="6" height="6"/><rect x="24" y="32" width="6" height="6"/><rect x="16" y="44" width="8" height="12"/></g></svg></div><p>Does the Hobart warehouse<br>have stock?</p></div>
<div class="abs question" style="left:616px"><div class="ring"><svg width="60" height="42" viewBox="0 0 60 42"><rect x="10" y="3" width="40" height="28" fill="none" stroke="var(--navy)" stroke-width="4"/><path d="M2 34h56l-4 6H6z" fill="var(--navy)"/></svg></div><p>How many do we need<br>to order?</p></div>
<div class="abs question" style="left:890px"><div class="ring"><svg width="62" height="48" viewBox="0 0 62 48" fill="none" stroke="var(--navy)" stroke-width="4"><path d="M2 2v44h58"/><path d="M10 36l14-14 10 10 20-20"/><path d="M44 10h12v12" stroke-width="4"/></svg></div><p>Why have we sold so much<br>of that product?</p></div>

<section class="abs process-side"></section>
<div class="abs process-photo" role="img" aria-label="Photo of hands pointing a pen at charts on a tablet over printed reports"></div>
<h2 class="abs process-title">Our Process</h2>
<p class="abs process-intro">For businesses on the Ledgerly platform who manage inventory, our Scoping Consultation is the first step to finally control your inventory with confidence.</p>
<div class="abs step" style="top:1471px"><div class="num">1</div><div><h3>Scoping</h3><p>We ensure what you are wanting to do is actually achievable, and make sure we have a good grip.</p></div></div>
<div class="abs step" style="top:1570px"><div class="num">2</div><div><h3>Implementation</h3><p>We ensure what you are wanting to do is actually achievable, and make sure we have a good grip.</p></div></div>
<div class="abs step" style="top:1671px"><div class="num">3</div><div><h3>Training</h3><p>We ensure what you are wanting to do is actually achievable, and make sure we have a good grip.</p></div></div>
<div class="abs step" style="top:1770px"><div class="num">4</div><div><h3>Support</h3><p>We ensure what you are wanting to do is actually achievable, and make sure we have a good grip.</p></div></div>

<h2 class="abs section-title" style="top:1998px;font-weight:600">Working with leading lights</h2>
<p class="abs clients-sub">Some of our many recent clients include</p>

<div class="abs client" style="left:99px;top:2118px">K7</div>
<div class="abs client" style="left:306px;top:2118px">Marlow HR</div>
<div class="abs client" style="left:514px;top:2118px">Brenvik</div>
<div class="abs client" style="left:721px;top:2118px"><i></i>Stonefield Builders</div>
<div class="abs client" style="left:929px;top:2118px">harrow quill</div>
<div class="abs client" style="left:99px;top:2238px">Fernlo</div>
<div class="abs client" style="left:306px;top:2238px"><i></i>Ledgerline</div>
<div class="abs client" style="left:514px;top:2238px">Quiet Lane</div>
<div class="abs client" style="left:721px;top:2238px">Pulsar</div>
<div class="abs client" style="left:929px;top:2238px">NOVRA</div>
<div class="abs client" style="left:99px;top:2358px">Clearmind</div>
<div class="abs client" style="left:306px;top:2358px">brightpath</div>
<div class="abs client" style="left:514px;top:2358px">Tidewell</div>
<div class="abs client" style="left:721px;top:2358px">Vine Atlas</div>
<div class="abs client" style="left:929px;top:2358px">gearwise</div>

<section class="abs band"></section>
<h2 class="abs band-title">Client Testimonials</h2>
<div class="abs quote" style="left:96px"><div class="avatar" role="img" aria-label="Portrait of client"></div><blockquote><b>“</b>Great follow up and support. Friendly and accessible. Thank you!<div class="who">Mara Pellow</div><div class="role">Director, Civic Relief Advisory</div></blockquote></div>
<div class="abs quote" style="left:455px"><div class="avatar" role="img" aria-label="Portrait of client"></div><blockquote><b>“</b>Fantastic service and a focus on ensuring value is delivered in a timely manner.<div class="who">Lucas Verhoven</div><div class="role">Director, Brightpath Partners</div></blockquote></div>
<div class="abs quote" style="left:826px"><div class="avatar" role="img" aria-label="Portrait of client"></div><blockquote><b>“</b>No sense in going it alone when these guys have seen it and done it<div class="who">Dean Haskell</div><div class="role">Director, Ledgerline</div></blockquote></div>

<h2 class="abs section-title" style="top:2992px;font-weight:600">Get In Touch</h2>
<h3 class="abs form-title">Web Contact Form - Vantrel Works :</h3>
<div class="abs field" style="left:99px;top:3114px;width:294px">Name :</div>
<div class="abs field" style="left:405px;top:3114px;width:297px">Phone :</div>
<div class="abs field" style="left:99px;top:3158px;width:294px">Email :</div>
<div class="abs field" style="left:405px;top:3158px;width:297px">Company :</div>
<div class="abs field" style="left:99px;top:3202px;width:603px;height:68px">Message :</div>
<div class="abs submit">SUBMIT</div>

<h3 class="abs info-title">Contact Information</h3>
<div class="abs info" style="top:3108px"><span class="ic"><svg width="12" height="16" viewBox="0 0 12 16"><path d="M6 0a6 6 0 0 1 6 6c0 4-6 10-6 10S0 10 0 6a6 6 0 0 1 6-6z" fill="var(--navy)"/><circle cx="6" cy="6" r="2" fill="#fff"/></svg></span><span>12/48 Harbour Rd, Melbourne, VIC, 3000<br>214 Ridgeview Parkway, Lakemont, CO</span></div>
<div class="abs info" style="top:3175px"><span class="ic"><svg width="14" height="14" viewBox="0 0 14 14"><path d="M3 0l3 4-2 2c1 2 2 3 4 4l2-2 4 3-2 3C6 14 0 8 0 2z" fill="var(--navy)"/></svg></span><span>+61 (03) 9000 1234 &nbsp;| &nbsp;+1 (720) 555 0142</span></div>
<div class="abs info" style="top:3224px"><span class="ic"><svg width="14" height="10" viewBox="0 0 14 10"><rect width="14" height="10" fill="var(--navy)"/><path d="M0 0l7 6 7-6" stroke="#fff" fill="none"/></svg></span><span>enquiries@vantrelworks.com</span></div>
<div class="abs social"><i style="background:#2f4f8f"></i><i style="background:#2fa6dc"></i><i style="background:#d93a2f"></i><i style="background:#9a7a55"></i></div>

<div class="abs rule"></div>
<p class="abs copy">Copyrights © 2017, Vantrel Works. All Rights Reserved.</p>

</body>
</html>
```